New Website Announcement

We need a flyer to announce our new website to customers and prospective clients. The website will be launching soon, but I can provide a detailed outline in PDF form with copy and imagery to serve as inspiration for this design.

I would like a postcard size document that can be mailed in an envelope (no need for postcard style mailer info on 1 side)

About my company:

Clarity Through Craft is a new breed of marketing consulting agency built for the next frontier of consumer learning. Social interaction will be at the heart of great insights going forward – in how consumers engage with brands and in how organizations socialize what they learn to gain competitive advantage.
By fusing innovative insights techniques, technology and compelling graphic design-based reporting, we ensure results get noticed and make an impact.

contact info that can also be included:

Email: dana@clarity-through-craft.example

Phone: 607-352-8814

New High Res logo file has been added. (.ai)

Thanks

Attention all designers submitting a design for this project. Please keep in mind a few important details about this project.

1. Remember that the main objective of this postcard is to announce my new website.

2. Please be sure to read the brief for the copy I would like on each side. You can be creative in how it is displayed, but I need this key information somewhere. All other copy on the attached files is for your background only.

3. Please do not submit overly simple designs that just take the images I provided and overlay a text box with my copy. I could easily do this myself in PowerPoint in 5 minutes.

4. Remember that the design should be edgy and modern but needs to be professional and speak to a business audience.

Please submit any questions. Thank you for your submissions. 

Dana

Illustrator high res logo file now correctly uploaded. Thanks.

Target Market(s)

senior level marketing and research clients at large companies and agencies

Industry/Entity Type

Marketing

Requirements
Must have
• Main message:

Need an engaging way to tell customers and prospective clients that we have a new website and that they should come visit us online to learn more about out services, check out case studies and read about our exciting partnerships.

COPY TO USE - UPDATED

Side 1:
(logo)
Introducing Clarity Through Craft

Let’s talk about taking research out of the dark ages.

Visit our newly launched website to learn how and get in touch.

www.clarity-through-craft.example

Side 2
Logo
followed by tagline:
Consumer insights that get noticed.
A leading-edge marketing partnership that really works.

Additional text to use on Side 2:
How we can help...

Think of us as your go-to resource for identifying and incorporating the most innovative and exciting techniques into your research programs. We carefully curate and develop close partnerships with the best of the best - from online qualitative research and mobile ethnography to social media listening and fresh takes on concept testing, we can guide the way.

Plus, we believe that socializing consumer learning is just as critical as gathering it.By taking insights deliverables to the next level – through infographics, videos, magazines,interactive profiles and so much more – we are getting stakeholders excited to engage with research and inspired to take action because of it.
It’s a new way to look at insights from a new type of partner. And, it’s a new way to get the most from your research dollars.
Nice to have
• could incorporate our website main image of the lamp on white brick background which is attached, but not 100% mandatory.
Should not have
• - should not be too playful or young, but needs to be modern and design focused

- should not be cluttered or overly 'salesy'

- needs to be upscale and elegant / compelling and aligned with the look and feel of the website imagery (see attached)

```html
<!DOCTYPE html>
<html lang="en">
<head>
<meta charset="utf-8">
<title>Clarity Through Craft – New Website Postcard</title>
<link rel="stylesheet" href="https://fonts.googleapis.com/css2?family=Cinzel:wght@500&family=Roboto+Condensed:wght@400;700&family=Ubuntu:wght@500;700&family=Arimo:wght@400;700&display=swap">
<style>
  :root {
    --backdrop: #e4e1dc;
    --blue: #1f72bf;
    --navy: #1b3566;
    --navy-light: #4189c6;
    --ink: #1f1f1f;
    --body-ink: #3a3a3a;
    --band: #e9e9e9;
    --rule: #2b2b2b;
    --wall-light: #fbfbfb;
    --wall-mid: #d9d9d9;
    --wall-dark: #b9b9b9;
    --badge-gold: #c9a24a;
  }
  * { box-sizing: border-box; margin: 0; padding: 0; }
  html, body { width: 1200px; height: 522px; overflow: hidden; background: var(--backdrop); }
  body { position: relative; font-family: "Arimo", Arial, sans-serif; color: var(--ink); }

  .card { position: absolute; overflow: hidden; background: var(--band); box-shadow: 0 3px 8px rgba(0,0,0,.35); }
  .card--front { left: 32px; top: 36px; width: 548px; height: 424px; }
  .card--back  { left: 614px; top: 66px; width: 552px; height: 428px; }

  .wall-photo { position: absolute; left: 0; top: 0; width: 100%; }
  .card--front .wall-photo {
    height: 330px;
    background:
      radial-gradient(ellipse 260px 170px at 80% 42%, var(--wall-light), rgba(255,255,255,0) 70%),
      linear-gradient(180deg, var(--wall-mid) 0%, #e6e6e6 55%, #d0d0d0 78%, #e2e2e2 100%);
  }
  .card--back .wall-photo {
    height: 390px;
    background:
      radial-gradient(ellipse 300px 200px at 50% 45%, #f7f7f7, rgba(255,255,255,0) 75%),
      linear-gradient(180deg, #dedede 0%, #ececec 60%, var(--wall-mid) 100%);
  }

  .wordmark {
    position: absolute; font-family: "Ubuntu", sans-serif; font-weight: 700;
    color: var(--blue); font-size: 22px; line-height: 23px; text-transform: uppercase; letter-spacing: .5px;
  }
  .card--front .wordmark { left: 30px; top: 30px; }
  .card--back .wordmark { left: 30px; top: 30px; }

  .social-links { position: absolute; right: 28px; top: 30px; display: flex; gap: 6px; }
  .social-links span { width: 18px; height: 18px; border-radius: 3px; background: var(--blue); border: 1.5px solid #fff; box-shadow: 0 0 0 1px var(--blue); }

  .headline {
    position: absolute; left: 0; width: 552px; top: 180px; text-align: center;
    font-family: "Cinzel", serif; font-weight: 500; font-size: 25px; line-height: 31px; color: var(--ink);
  }

  .visit-band {
    position: absolute; left: 0; top: 330px; width: 100%; height: 62px;
    border-top: 2px solid var(--rule); background: linear-gradient(180deg, #f2f2f2, #dcdcdc);
    text-align: center; font-family: "Roboto Condensed", sans-serif;
  }
  .visit-band .invite { font-weight: 700; font-size: 17px; color: var(--ink); margin-top: 10px; }
  .visit-band .url { font-weight: 700; font-size: 20px; color: var(--blue); margin-top: 2px; }

  .contact-bar {
    position: absolute; left: 0; bottom: 0; width: 100%; height: 32px;
    background: linear-gradient(90deg, var(--navy) 0%, var(--navy-light) 48%, var(--navy) 100%);
    color: #fff; display: flex; align-items: center; justify-content: space-between; padding: 0 30px;
    font-family: "Roboto Condensed", sans-serif;
  }
  .contact-bar .phone { font-weight: 700; font-size: 16px; display: flex; align-items: center; gap: 5px; }
  .contact-bar .email { font-size: 13px; display: flex; align-items: center; gap: 5px; }
  .contact-bar .mark-dot { width: 12px; height: 12px; border-radius: 50%; background: #fff; margin-left: 60px; }

  .tagline {
    position: absolute; right: 27px; top: 32px; text-align: right;
    font-family: "Ubuntu", sans-serif; font-weight: 700; font-size: 19px; line-height: 23px; color: var(--ink);
  }

  .pillar { position: absolute; top: 102px; width: 132px; margin-left: -66px; text-align: center; }
  .pillar-label {
    height: 24px; line-height: 24px; background: rgba(255,255,255,.75);
    box-shadow: 0 1px 3px rgba(0,0,0,.2);
    font-family: "Roboto Condensed", sans-serif; font-weight: 700; font-size: 11px; color: var(--blue);
  }
  .pillar-icon {
    width: 62px; height: 62px; margin: 8px auto 0; border-radius: 50%;
    background: radial-gradient(circle at 40% 35%, #fff, #d6d6d6 80%);
    box-shadow: 0 2px 5px rgba(0,0,0,.3); display: flex; align-items: center; justify-content: center;
  }
  .pillar--award { left: 95px; }
  .pillar--design { left: 276px; }
  .pillar--partners { left: 458px; }
  .award-badge { width: 28px; height: 28px; background: var(--badge-gold); border-radius: 4px; }
  .partner-shape { width: 26px; height: 26px; border-radius: 50%; background: var(--blue); }

  .story {
    position: absolute; left: 27px; top: 212px; width: 498px; height: 167px;
    background: rgba(245,245,245,.9); border: 1px solid #b8b8b8; padding: 12px 30px 0 28px;
  }
  .story-pointer { position: absolute; top: -12px; left: 420px; }
  .story h2 { font-family: "Arimo", sans-serif; font-weight: 700; font-size: 14.5px; color: var(--ink); margin-bottom: 4px; }
  .story p { font-size: 9.2px; line-height: 11.5px; color: var(--body-ink); margin-bottom: 11px; text-align: justify; }

  .site-bar {
    position: absolute; left: 0; bottom: 0; width: 100%; height: 38px;
    border-top: 2px solid var(--rule);
    background: linear-gradient(90deg, var(--navy) 0%, var(--navy-light) 50%, var(--navy) 100%);
    color: #fff; text-align: center; line-height: 36px;
    font-family: "Roboto Condensed", sans-serif; font-weight: 700; font-size: 20px;
  }
</style>
</head>
<body>

<section class="card card--front" aria-label="Postcard front">
  <div class="wall-photo" role="img" aria-label="White brick wall with a black arc floor lamp casting light"></div>
  <div class="wordmark">Clarity<br>Through Craft</div>
  <div class="social-links" aria-label="Social channels"><span></span><span></span><span></span></div>
  <h1 class="headline">Let’s talk about taking<br>Research out of the dark ages.</h1>
  <div class="visit-band">
    <p class="invite">Visit our newly launched website to learn how and get in touch</p>
    <p class="url">www.clarity-through-craft.example</p>
  </div>
  <footer class="contact-bar">
    <span class="phone">
      <svg width="14" height="14" viewBox="0 0 14 14" aria-hidden="true"><circle cx="7" cy="7" r="6" fill="none" stroke="#fff" stroke-width="1.2"/><path d="M5 4 L6 6 L5.3 6.8 Q6 8.3 7.3 8.8 L8 8 L10 9 L9.4 10.3 Q6.5 10.5 4.2 7.2 Q3.8 5 5 4Z" fill="#fff"/></svg>
      607-352-8814
    </span>
    <span class="mark-dot" aria-hidden="true"></span>
    <span class="email">
      <svg width="13" height="9" viewBox="0 0 13 9" aria-hidden="true"><rect x=".5" y=".5" width="12" height="8" fill="#fff"/><path d="M.5 .5 L6.5 5 L12.5 .5" fill="none" stroke="#1b3566" stroke-width="1"/></svg>
      dana@clarity-through-craft.example
    </span>
  </footer>
</section>

<section class="card card--back" aria-label="Postcard back">
  <div class="wall-photo" role="img" aria-label="Softly lit white brick wall background"></div>
  <div class="wordmark">Clarity<br>Through Craft</div>
  <h2 class="tagline">Consumer insights<br>that get noticed.</h2>

  <div class="pillar pillar--award">
    <div class="pillar-label">AWARD-WINNING INSIGHTS</div>
    <div class="pillar-icon"><span class="award-badge"></span></div>
  </div>
  <div class="pillar pillar--design">
    <div class="pillar-label">COMPELLING DESIGN</div>
    <div class="pillar-icon">
      <svg width="40" height="32" viewBox="0 0 40 32" aria-hidden="true">
        <g stroke="#333" stroke-width="2" stroke-linecap="round"><line x1="20" y1="2" x2="20" y2="7"/><line x1="10" y1="5" x2="12" y2="9"/><line x1="30" y1="5" x2="28" y2="9"/></g>
        <path d="M3 20 Q20 6 37 20 Q20 34 3 20Z" fill="#fff" stroke="#333" stroke-width="2"/>
        <circle cx="20" cy="20" r="7" fill="var(--blue)"/><circle cx="20" cy="20" r="3" fill="#222"/>
      </svg>
    </div>
  </div>
  <div class="pillar pillar--partners">
    <div class="pillar-label">EXPERT PARTNERS</div>
    <div class="pillar-icon"><span class="partner-shape"></span></div>
  </div>

  <article class="story">
    <svg class="story-pointer" width="24" height="13" viewBox="0 0 24 13" aria-hidden="true"><path d="M0 12.5 L12 0.5 L24 12.5" fill="#f5f5f5" stroke="#b8b8b8"/></svg>
    <h2>A New Way to Look at Insights from a New Type of Partner</h2>
    <p>Think of us as your go-to resource for identifying and incorporating the most innovative and exciting techniques into your research programs. We carefully curate and develop close partnerships with the best of the best. From online qualitative research and mobile ethnography to social media listening and fresh takes on concept testing, we can guide the way.</p>
    <p>Plus, we believe that socializing consumer learning is just as critical as gathering it. By taking insights deliverables to the next level - through infographics, videos, magazines, interactive profiles and so much more. We are getting stakeholders excited to engage with research and inspired to take action.</p>
    <p>It’s a new way to get the most from your research dollars...from a new type of partner.</p>
  </article>

  <footer class="site-bar">www.clarity-through-craft.example</footer>
</section>

</body>
</html>
```